Chiropractic healthcare group business card

We are a Portland Oregon based chiropractic healthcare group. Looking for a new business card design. Something cutting edge, that shows off our new logo and tag line.Use either of the attached logos.Our tag line = "Move freely and live fully again?"I'm open to about anything, impress me!!
Target Market(s)
Chiropractic patients - Auto injury, back pain, sports injuries, neck , shoulder, hip, knee, ankle pain.
Industry/Entity Type
Chiropractic
Contact Information for Business Card
Dr. Bram Tovelund, D.C.
Clinic name - Cedar Chiropractic
2 clinics
location #1
20418 NW Harlow Road
Suite B
North Plains, OR 97133
Location #2
13529 SE Marston Street
Fernbrook OR 97251
Main phone line 971.386.4217
website : www.BirchValeCare.com
Tag line "Move freely and live fully again?"
Colors
Designer to choose colors to be used in the design.
Requirements
Must have
- Use the logo colors -- Want the orange color to be a TRUE orange.
- Both clinic address
- phone number
- website
- personal email - b.tovelund@FreshStrideHealth.com
- tag line - "Move freely and live fully again?"

```html
<!DOCTYPE html>
<html lang="en">
<head>
<meta charset="utf-8">
<title>Cedar Chiropractic – Business Card</title>
<link rel="stylesheet" href="https://fonts.googleapis.com/css2?family=Roboto:wght@400;500&display=swap">
<style>
  :root {
    --orange: #f39a1e;
    --orange-deep: #ef8a14;
    --orange-light: #f2b04a;
    --grey-text: #4a4a4a;
    --grey-mid: #6d6d6d;
    --grey-line: #8a8a8a;
    --paper: #ffffff;
    --backdrop: #e6e6e6;
  }
  * { box-sizing: border-box; margin: 0; padding: 0; }
  html, body { width: 893px; height: 1200px; overflow: hidden; }
  body {
    background: var(--backdrop);
    font-family: "Roboto", Arial, sans-serif;
    position: relative;
  }
  .card {
    position: absolute;
    left: 86px;
    width: 720px;
    height: 411px;
    border-radius: 18px;
    overflow: hidden;
    box-shadow: 0 10px 30px rgba(0,0,0,.18);
  }
  .card-front { top: 120px; background: var(--paper); }
  .card-back {
    top: 670px;
    background: radial-gradient(ellipse at 55% 45%, var(--orange-light) 0%, var(--orange) 60%, var(--orange-deep) 100%);
  }

  /* Front */
  .brand {
    position: absolute; left: 56px; top: 84px;
    display: flex; align-items: center; gap: 12px;
  }
  .brand-dot { width: 18px; height: 18px; border-radius: 50%; background: var(--orange); flex: none; }
  .brand-name { font-size: 26px; font-weight: 500; color: var(--grey-text); letter-spacing: .5px; line-height: 1; }

  .doctor {
    position: absolute; left: 56px; top: 188px;
    font-size: 25px; font-weight: 500; color: var(--orange); letter-spacing: .3px;
  }
  .doctor .credential { color: var(--grey-mid); font-weight: 400; }
  .doctor-rule { position: absolute; left: 56px; top: 234px; width: 42px; height: 2px; background: var(--grey-line); }
  .contact { position: absolute; left: 56px; top: 250px; list-style: none; }
  .contact li {
    display: flex; align-items: center; gap: 10px;
    font-size: 16px; color: var(--grey-text); line-height: 26px;
  }
  .contact svg { width: 14px; height: 14px; fill: var(--orange); flex: none; }

  .locations {
    position: absolute; right: 40px; top: 56px; text-align: right;
    font-size: 16px; color: var(--grey-text); line-height: 23px;
  }
  .locations .location + .location { margin-top: 4px; }

  .front-bands { position: absolute; left: 0; bottom: 0; width: 720px; height: 120px; }
  .website {
    position: absolute; right: 44px; bottom: 34px;
    font-size: 17px; color: var(--paper); letter-spacing: .3px; line-height: 1;
  }

  /* Back */
  .back-brand {
    position: absolute; left: 0; right: 0; top: 132px;
    display: flex; justify-content: center; align-items: center; gap: 14px;
  }
  .back-brand .brand-name { font-size: 40px; color: var(--paper); letter-spacing: 1px; }
  .back-brand .brand-dot { width: 26px; height: 26px; background: var(--paper); }
  .tagline-rule {
    position: absolute; left: 230px; top: 232px; width: 260px; height: 2px;
    background: linear-gradient(90deg, rgba(255,255,255,0), #fff 50%, rgba(255,255,255,0));
  }
  .tagline {
    position: absolute; left: 0; right: 0; top: 252px; text-align: center;
    font-size: 22px; color: var(--paper); letter-spacing: .4px;
  }
</style>
</head>
<body>

<section class="card card-front" aria-label="Business card front">
  <div class="brand">
    <span class="brand-dot"></span>
    <span class="brand-name">Cedar Chiropractic</span>
  </div>

  <h1 class="doctor">DR. BRAM TOVELUND, <span class="credential">D.C.</span></h1>
  <div class="doctor-rule"></div>
  <ul class="contact">
    <li>
      <svg viewBox="0 0 24 24" aria-hidden="true"><path d="M6.6 10.8a15.1 15.1 0 0 0 6.6 6.6l2.2-2.2a1 1 0 0 1 1-.25 11.4 11.4 0 0 0 3.6.57 1 1 0 0 1 1 1V20a1 1 0 0 1-1 1A17 17 0 0 1 3 4a1 1 0 0 1 1-1h3.5a1 1 0 0 1 1 1c0 1.25.2 2.45.57 3.57a1 1 0 0 1-.25 1z"/></svg>
      971.386.4217
    </li>
    <li>
      <svg viewBox="0 0 24 24" aria-hidden="true"><path d="M2 5h20v14H2z"/><path d="M2 5l10 8 10-8" fill="none" stroke="#fff" stroke-width="2"/></svg>
      b.tovelund@FreshStrideHealth.com
    </li>
  </ul>

  <div class="locations">
    <p class="location">Location #2 :<br>13529 SE Marston Street<br>Fernbrook OR 97251</p>
    <p class="location">location #1:<br>20418 NW Harlow Road<br>Suite C, Alder Ridge, OR 97190</p>
  </div>

  <svg class="front-bands" viewBox="0 0 720 120" aria-hidden="true">
    <path d="M0 96 L420 96 L452 70" fill="none" stroke="var(--grey-line)" stroke-width="5"/>
    <path d="M0 106 L440 106 C456 106 464 100 472 90 L494 56 C502 45 512 40 528 40 L720 40 L720 120 L0 120 Z" fill="var(--orange)"/>
  </svg>
  <p class="website">www.BirchValeCare.com</p>
</section>

<section class="card card-back" aria-label="Business card back">
  <div class="back-brand">
    <span class="brand-dot"></span><span class="brand-name">Cedar Chiropractic</span>
  </div>
  <div class="tagline-rule"></div>
  <p class="tagline">Move freely and live fully again</p>
</section>

</body>
</html>
```